*YO!!! Designers Needed!!* Front Page Cover Needed for a $$Billion Dollar$$ Company

We are a manufacturer of aluminum electrolytic capacitors. We are looking to create a front page cover that will be used on our annual report. We are a publicly listed company and work with many Pinnacle 300 companies, so your work will be viewed by the BIG GUNS and EXECUTIVES around the WORLD! If selected, you may be selected for additional work.

The front page cover should be unique. If elegance, modern, bling, and creativity somehow got together and had a child, that's what the cover page would look like!

Inspired Examples attached. Check them out!

www.velmoro.com

Font styles to use
Sans Serif

Requirements
Must have
• 1. Must include the attached logo. Logo size, color, and placement are at your discretion.

2. Should include the text, '2020 Annual Report'

3. The design should incorporate the use of foil and/or be embossed. The foil can be part of the design or can be the full page. See various examples attached for reference.

4. Shall be in A4 size and vertical orientation.
Nice to have
• Feel free to add any icons or stock photos (for example capacitors or circuit boards) if needed.

Be creative here and don't be afraid to be bold! The end product will be printed and budget is not a limiting factor, so feel free to make it extravagant if needed.

Our slogan is "Think Ahead". This slogan can or cannot be part of the theme.

```html
<!DOCTYPE html>
<html lang="en">
<head>
<meta charset="utf-8">
<title>Velmoro 2020 Annual Report Cover</title>
<link rel="stylesheet" href="https://fonts.googleapis.com/css2?family=Jost:wght@400;600&display=swap">
<style>
  :root {
    --stage: #2a2622;
    --cover: #080808;
    --gold: #c9a04a;
    --gold-light: #f1d58c;
    --gold-deep: #a67c2c;
    --ink: #141414;
  }
  * { margin: 0; padding: 0; box-sizing: border-box; }
  html, body {
    width: 1200px;
    height: 789px;
    overflow: hidden;
    background: var(--stage);
  }
  .canvas {
    position: relative;
    width: 1200px;
    height: 789px;
    display: flex;
    align-items: center;
    justify-content: center;
  }
  .cover {
    position: relative;
    width: 516px;
    height: 729px;
    background: var(--cover);
    box-shadow: 0 10px 30px rgba(0,0,0,0.5);
  }
  .masthead {
    position: absolute;
    left: 0;
    top: 118px;
    width: 100%;
    height: 200px;
  }
  .foil-band {
    position: absolute;
    left: 68px;
    top: 52px;
    width: 390px;
    height: 96px;
    border-radius: 20px 40px 28px 14px;
    background: linear-gradient(100deg, var(--gold-deep) 0%, var(--gold-light) 35%, var(--gold) 60%, var(--gold-light) 80%, var(--gold-deep) 100%);
  }
  .gold-frame {
    position: absolute;
    left: 170px;
    top: 0;
    width: 200px;
    height: 200px;
    border: 1.5px solid var(--gold);
  }
  .company-name {
    position: absolute;
    left: 0;
    top: 78px;
    width: 100%;
    text-align: center;
    font-family: 'Jost', sans-serif;
    font-weight: 600;
    font-size: 44px;
    line-height: 1;
    color: var(--ink);
  }
  .report-title {
    position: absolute;
    left: 0;
    bottom: 92px;
    width: 100%;
    text-align: center;
    font-family: 'Jost', sans-serif;
    font-weight: 400;
    font-size: 19px;
    letter-spacing: 0.38em;
    color: var(--gold);
  }
</style>
</head>
<body>
  <main class="canvas">
    <section class="cover">
      <div class="masthead">
        <div class="foil-band" role="img" aria-label="Gold foil brush stroke band across the cover"></div>
        <div class="gold-frame"></div>
        <p class="company-name">Velmoro</p>
      </div>
      <h1 class="report-title">2020 ANNUAL REPORT</h1>
    </section>
  </main>
</body>
</html>
```